Executive Summary

Create a one page executive summary of a venture fund - with the information here:
https://files.brindlepath.net/doc/7qR2mXvT9kLp4sWn8yZcB3fHj6dKa5eU/view?share=open

```html
<!DOCTYPE html>
<html lang="en">
<head>
<meta charset="utf-8">
<title>Executive Summary</title>
<link rel="stylesheet" href="https://fonts.googleapis.com/css2?family=Gelasio:wght@400;500&family=Mulish:wght@400;600;700&display=swap">
<style>
:root{
  --wine:#7f1428;
  --ink:#4a4a4a;
  --ink-dark:#3a3a3a;
  --blush:#f5eff0;
  --strip:#f6f5f5;
  --paper:#ffffff;
}
*{margin:0;padding:0;box-sizing:border-box}
html,body{width:950px;height:1200px;overflow:hidden;background:var(--paper)}
.sheet{position:relative;width:950px;height:1200px;overflow:hidden;background:var(--paper);font-family:"Mulish",sans-serif;color:var(--ink)}
.serif{font-family:"Gelasio",serif;font-weight:400;color:var(--wine)}
.blush-disc{position:absolute;left:544px;top:-104px;width:432px;height:432px;border-radius:50%;background:var(--blush)}
.header-icon{position:absolute;left:25px;top:22px}
.page-title{position:absolute;left:84px;top:36px;font-size:39px;line-height:1;letter-spacing:.2px}
.bio-card{position:absolute;left:26px;top:136px;width:370px;height:190px;border-radius:22px;background:#fff;box-shadow:0 1px 8px rgba(0,0,0,.14),inset 0 0 0 1px #eee;padding:26px 14px 0 14px}
.bio-name{font-size:24px;line-height:1.1;margin-left:0}
.bio-role{font-size:17.5px;line-height:1.2;margin:6px 0 0 -2px}
.bio-text{font-size:13px;line-height:27.5px;margin-top:6px;color:var(--ink)}
.section-head{position:absolute;left:25px;font-size:21px;line-height:1}
.checklist{position:absolute;left:25px;top:387px;list-style:none;width:380px}
.checklist li{position:relative;padding-left:21px;font-size:13.2px;line-height:18.5px;margin-bottom:5px}
.checklist li svg{position:absolute;left:0;top:3px}
.portrait{position:absolute;left:458px;top:134px;width:472px;height:445px;background:linear-gradient(180deg,#2a2320 0%,#6e5246 45%,#d0b4a3 65%,#1f1b1c 100%)}
.portfolio-head{position:absolute;left:25px;top:532px;font-size:25px;line-height:1}
.company-band{position:absolute;left:15px;top:579px;width:915px;height:41px;background:var(--wine);color:#fff;font-size:18px;line-height:41px;padding-left:11px}
.company-strip{position:absolute;left:15px;top:620px;width:915px;height:30px;background:var(--strip)}
.company-copy{position:absolute;left:25px;top:662px;width:905px;font-size:13.6px;line-height:27.5px;color:var(--ink)}
.company-copy p{margin:0}
.company-copy .quote{margin-top:8px}
.fund-head{position:absolute;left:25px;top:896px;font-size:18px;line-height:1}
.fund-list{position:absolute;left:25px;top:922px;list-style:none}
.fund-list li{position:relative;padding-left:20px;font-size:13.8px;line-height:27.7px;color:var(--ink)}
.fund-list li::before{content:"";position:absolute;left:0;top:11px;border-left:4px solid var(--wine);border-top:3px solid transparent;border-bottom:3px solid transparent}
.contact{position:absolute;right:20px;top:1098px;text-align:right}
.contact-title{font-size:24px;line-height:1}
.contact-line{font-size:14px;margin-top:9px;color:var(--ink)}
.contact-name{font-size:12.5px;font-weight:700;margin-top:6px;color:var(--ink-dark);margin-right:4px}
.footer-rule{position:absolute;left:0;bottom:0;width:950px;height:6px;background:var(--wine)}
</style>
</head>
<body>
<div class="sheet">
  <div class="blush-disc"></div>

  <svg class="header-icon" width="44" height="60" viewBox="0 0 44 60" fill="none" stroke="#7f1428" stroke-width="2">
    <rect x="4" y="4" width="38" height="54" rx="3"/>
    <path d="M4 8 Q4 1 10 1 H40"/>
    <line x1="9" y1="4" x2="9" y2="58"/>
    <circle cx="26" cy="24" r="8"/>
    <circle cx="26" cy="21.5" r="3"/>
    <path d="M20.5 29 Q26 24 31.5 29"/>
    <line x1="18" y1="40" x2="34" y2="40"/>
    <line x1="21" y1="45" x2="31" y2="45"/>
  </svg>
  <h1 class="page-title serif">Executive Summary</h1>

  <section class="bio-card">
    <h2 class="bio-name serif">Mira Lindqvist</h2>
    <p class="bio-role serif">CFA, Vice President (California)</p>
    <p class="bio-text">Veteran investor in energy transition. 10+ years of experience in capital markets, energy, sustainability and innovations. M.S. from Halbrook University</p>
  </section>

  <h2 class="section-head serif" style="top:345px">Lorem Ipsum Dolor Sit Ametsec.</h2>
  <ul class="checklist">
    <li><svg width="13" height="13" viewBox="0 0 13 13" fill="none" stroke="#555" stroke-width="1.3"><circle cx="6" cy="7" r="5"/><path d="M3.5 6.5 L6 9.5 L12 1.5" stroke="#7f1428" stroke-width="1.6"/></svg>Laoreet dolore magna aliquam erat volutpatt wore nim veniam, quit.</li>
    <li><svg width="13" height="13" viewBox="0 0 13 13" fill="none" stroke="#555" stroke-width="1.3"><circle cx="6" cy="7" r="5"/><path d="M3.5 6.5 L6 9.5 L12 1.5" stroke="#7f1428" stroke-width="1.6"/></svg>Laoreet dolore magna aliquam erat volutpatt dummy</li>
    <li><svg width="13" height="13" viewBox="0 0 13 13" fill="none" stroke="#555" stroke-width="1.3"><circle cx="6" cy="7" r="5"/><path d="M3.5 6.5 L6 9.5 L12 1.5" stroke="#7f1428" stroke-width="1.6"/></svg>Laoreet dolore magna aliquam erat volutpatt wore nim veniam, quit.</li>
    <li><svg width="13" height="13" viewBox="0 0 13 13" fill="none" stroke="#555" stroke-width="1.3"><circle cx="6" cy="7" r="5"/><path d="M3.5 6.5 L6 9.5 L12 1.5" stroke="#7f1428" stroke-width="1.6"/></svg>Laoreet dolore magna aliquam erat volutpatt</li>
  </ul>

  <div class="portrait" role="img" aria-label="Portrait photograph of the vice president"></div>

  <h2 class="portfolio-head serif">Example Portfolio Startups</h2>
  <div class="company-band serif">Corvanta: Modular Green Methanol Production</div>
  <div class="company-strip"></div>
  <div class="company-copy">
    <p>The Northgate Tech Spin out company has developed a proprietary process to synthesize commodity chemicals, starting with green methanol and ammonia, at cost-parity using used diesel engines.</p>
    <p>By converting these engines to consume inputs such as methane, biogas, and carbon dioxide, the company has created a low-carbon process to produce these chemicals by displacing the need for flaring or release of methane, plugging into waste streams offsite.</p>
    <p class="quote">It has been a pleasure working with Meridian Arc Capital and having them on our cap table. Their team is well connected, always available and eager to help.</p>
  </div>

  <h2 class="fund-head serif">Fund I Investments So Far (Continue )to Invest</h2>
  <ul class="fund-list">
    <li>Luxora, former Trivex Nano (Seed, raising Series A)</li>
    <li>Corvanta (Seed, raising Series A)</li>
    <li>Reclaima (Series A, will raise Series B)</li>
    <li>Nutrisyne (Seed)</li>
    <li>Corvanta Sola Biofuels (Pre-seed)</li>
    <li>VoltWay (Seed)</li>
  </ul>

  <div class="contact">
    <h2 class="contact-title serif">Join Us</h2>
    <p class="contact-line">For Any Inquiries, Please Contact:</p>
    <p class="contact-name">Dana Whitlock, Managing Partner</p>
  </div>

  <div class="footer-rule"></div>
</div>
</body>
</html>
```